General Dental Office Business Card

I run a private general dental office in southern California, and would like a refresh/redesign of my business card. I focus on quality care rather than volume. The email address on the uploaded current card should be updated to: info@marbleshoredental.example. The current card's logo is a deboss, but I am open to other ideas. The logo can be refreshed, but it is something that's been with me since the beginning of the office, so I wouldn't want a drastic redesign.
Target Market(s)
Adults 18-99, whoever needs dental services
Industry/Entity Type
Healthcare/Dental
Contact Information for Business Card
Name, Address, Phone, email
Colors
Designer to choose colors to be used in the design.
Requirements
Must have
- Logo (Same as original one in the uploaded file), space on back for appointment time/date

```html
<!DOCTYPE html>
<html lang="en">
<head>
<meta charset="utf-8">
<title>Marble Shore Dental – Business Card</title>
<link href="https://fonts.googleapis.com/css2?family=Montserrat:wght@300;400&display=swap" rel="stylesheet">
<style>
  :root {
    --page: #ffffff;
    --card-back: #f3f4f6;
    --card-front: #ffffff;
    --teal: #5fc6d3;
    --teal-deep: #2aa9c0;
    --ink-blue: #1a8fb0;
    --ink-dark: #333333;
    --ink-grey: #6f6f6f;
    --rule: #8a8a8a;
  }
  * { margin: 0; padding: 0; box-sizing: border-box; }
  html, body { width: 837px; height: 1200px; overflow: hidden; background: var(--page); }
  body { font-family: "Montserrat", sans-serif; font-weight: 300; position: relative; }

  .card {
    position: absolute; top: 291px; width: 353px; height: 618px; overflow: hidden;
    box-shadow: 3px 5px 8px rgba(0,0,0,0.22);
  }
  .card--back { left: 41px; background: var(--card-back); }
  .card--front { left: 443px; background: var(--card-front); }

  .mark-area { position: absolute; inset: 0; width: 100%; height: 100%; }

  /* Back: appointment fields */
  .field { position: absolute; left: 29px; width: 295px; border-top: 1px solid var(--rule);
    text-align: center; color: var(--ink-grey); font-size: 15px; padding-top: 6px; letter-spacing: 0.3px; }
  .field--date { top: 54px; }
  .field--time { top: 122px; }

  .brand { position: absolute; color: #ffffff; font-weight: 400; line-height: 1; white-space: nowrap; }
  .brand span { display: block; }
  .brand--vertical { left: 52px; top: 490px; transform: rotate(-90deg); transform-origin: left top; font-size: 30px; }
  .brand--vertical .brand__sub { text-align: right; font-size: 25px; margin-top: 2px; }
  .brand--horizontal { left: 12px; top: 210px; width: 190px; text-align: center; font-size: 24px; }
  .brand--horizontal .brand__sub { font-size: 21px; margin-top: 2px; }

  /* Front: identity + contact */
  .identity { position: absolute; right: 27px; top: 28px; text-align: right; }
  .identity__name { color: var(--ink-blue); font-size: 26px; font-weight: 400; line-height: 1.1; }
  .identity__role { color: var(--ink-dark); font-size: 17px; font-weight: 400; margin-top: 2px; }

  .contact { position: absolute; right: 27px; top: 478px; text-align: right; font-size: 15px; line-height: 24px; list-style: none; }
  .contact__address { color: var(--ink-blue); }
  .contact__phone, .contact__link { color: var(--ink-grey); }
  .contact__link { font-size: 14px; }
  .contact__icon { display: inline-block; width: 12px; height: 12px; vertical-align: -1px; margin-right: 10px; }
</style>
</head>
<body>

<section class="card card--back" aria-label="Card back: appointment reminder">
  <svg class="mark-area" viewBox="0 0 353 618" role="img" aria-label="Watercolour teal mascot silhouette of the practice">
    <defs>
      <linearGradient id="tealBack" x1="0" y1="0" x2="0" y2="1">
        <stop offset="0" stop-color="var(--teal-deep)"/>
        <stop offset="0.25" stop-color="var(--teal)"/>
        <stop offset="1" stop-color="var(--teal)"/>
      </linearGradient>
    </defs>
    <path d="M0 190 Q60 170 110 150 L200 160 Q230 230 225 330 L290 618 L0 618 Z" fill="url(#tealBack)"/>
  </svg>
  <div class="field field--date">Appointment Date</div>
  <div class="field field--time">Time</div>
  <div class="brand brand--vertical"><span class="brand__main">Marble Shore</span><span class="brand__sub">Dental</span></div>
</section>

<section class="card card--front" aria-label="Card front: contact details">
  <svg class="mark-area" viewBox="0 0 353 618" role="img" aria-label="Watercolour teal mascot silhouette of the practice">
    <defs>
      <linearGradient id="tealFront" x1="1" y1="0" x2="0" y2="1">
        <stop offset="0" stop-color="var(--teal-deep)"/>
        <stop offset="0.3" stop-color="var(--teal)"/>
        <stop offset="1" stop-color="var(--teal)"/>
      </linearGradient>
    </defs>
    <path d="M0 232 Q70 180 195 165 L197 290 Q140 330 110 420 Q50 520 20 618 L0 618 Z" fill="url(#tealFront)"/>
  </svg>

  <header class="identity">
    <h1 class="identity__name">Helen M. Park DDS</h1>
    <p class="identity__role">General Dentistry</p>
  </header>

  <div class="brand brand--horizontal"><span class="brand__main">Marble Shore</span><span class="brand__sub">Dental</span></div>

  <ul class="contact">
    <li class="contact__address">1820 Coral Crest Drive</li>
    <li class="contact__address">Seabrook, CA 92700</li>
    <li class="contact__phone">949-555-0142</li>
    <li class="contact__link">
      <svg class="contact__icon" viewBox="0 0 12 12" aria-hidden="true"><path d="M0 4 L6 0 L12 4 L12 12 L0 12 Z" fill="var(--ink-blue)"/><path d="M0 5 L6 9 L12 5" fill="none" stroke="#fff" stroke-width="1.2"/></svg>info@marbleshoredental.example
    </li>
    <li class="contact__link">
      <svg class="contact__icon" viewBox="0 0 12 12" aria-hidden="true"><circle cx="6" cy="6" r="5" fill="none" stroke="var(--ink-blue)" stroke-width="1.6"/><path d="M5 4 L10 9 L7.5 9 L6.5 11 Z" fill="var(--ink-blue)"/></svg>www.marbleshoredental.example
    </li>
  </ul>
</section>

</body>
</html>
```